Logo is done, need templates now

I want to be able to have an email template, same for word documents, powerpoint etc. I have the logo, now I need all the pieces for appearance in correspondence and marketing

Target Market(s)

Professional Advisors and Wealthy Clients

Font styles to use
Serif

Requirements
Must have
• I want to be able to do word documents and email them with letterhead. I need great email signatures. I need similar formatting for the word documents to be flexible to add to powerpoint and other presentations.

```html
<!DOCTYPE html>
<html lang="en">
<head>
<meta charset="utf-8">
<title>Hollis Crest – Stationery</title>
<link href="https://fonts.googleapis.com/css2?family=Lato:wght@400;700&display=swap" rel="stylesheet">
<style>
  :root {
    --stage: #5c5c5c;
    --paper: #ffffff;
    --ink: #1e1e1e;
    --ink-soft: #555555;
    --gold: #b98a55;
    --gold-light: #e4c9a0;
    --gold-faint: #f6f1ea;
    --rule: #3a3a3a;
  }
  * { margin: 0; padding: 0; box-sizing: border-box; }
  html, body { width: 800px; height: 1200px; overflow: hidden; }
  body {
    background: var(--stage);
    position: relative;
    font-family: "Lato", sans-serif;
    color: var(--ink);
  }

  /* Letterhead */
  .letterhead {
    position: absolute;
    left: 146px; top: 117px;
    width: 508px; height: 762px;
    background: var(--paper);
  }
  .brand-name {
    font-family: "Lato", sans-serif;
    font-weight: 400;
    color: var(--gold);
    text-transform: uppercase;
    white-space: nowrap;
  }
  .letterhead__brand {
    position: absolute;
    top: 30px; left: 0; width: 100%;
    text-align: center;
    font-size: 13px;
    letter-spacing: 4px;
  }
  .letterhead__backdrop {
    position: absolute;
    top: 330px; left: 0; width: 100%;
    text-align: center;
    font-size: 44px;
    letter-spacing: 8px;
    color: var(--gold-faint);
  }
  .letterhead__footer {
    position: absolute;
    left: 0; right: 0; top: 711px;
    text-align: center;
    font-size: 10.4px;
  }
  .letterhead__address { line-height: 14px; }
  .letterhead__rule {
    width: 334px; height: 1px;
    margin: 3px auto 5px;
    background: var(--rule);
  }
  .letterhead__contact b { font-weight: 700; }

  /* Email signature */
  .signature {
    position: absolute;
    left: 146px; top: 966px;
    width: 508px; height: 152px;
    background: var(--paper);
    overflow: hidden;
  }
  .signature__details {
    position: absolute;
    left: 21px; top: 42px;
  }
  .signature__name {
    color: var(--gold);
    font-weight: 700;
    font-size: 16px;
    line-height: 18px;
  }
  .signature__role { font-size: 12.5px; line-height: 14px; }
  .signature__address {
    font-size: 12.5px; color: var(--ink-soft);
    margin-top: 5px; line-height: 16px;
  }
  .signature__contact { font-size: 12.5px; margin-top: 4px; line-height: 16px; }
  .signature__contact b { font-weight: 700; }
  .signature__web {
    font-size: 12.5px; color: var(--gold);
    margin-top: 5px; line-height: 16px;
  }
  .signature__brand {
    position: absolute;
    right: 20px; top: 48px;
    width: 140px; text-align: center;
    font-size: 10px; letter-spacing: 2.6px;
  }
  .signature__band {
    position: absolute;
    left: 268px; right: 0; bottom: 0;
    height: 31px;
    background: linear-gradient(90deg, var(--gold) 0%, var(--gold-light) 55%, var(--gold) 100%);
    clip-path: polygon(26px 0, 100% 0, 100% 100%, 0 100%);
    display: flex; align-items: center;
    padding-left: 31px;
    font-size: 12.5px; color: #3a3a3a;
  }
  .social-list { display: flex; gap: 2px; margin: 0 5px 0 5px; }
  .social-list svg { display: block; }
</style>
</head>
<body>

<section class="letterhead">
  <div class="letterhead__brand brand-name">Hollis Crest</div>
  <div class="letterhead__backdrop brand-name" aria-hidden="true">Hollis Crest</div>
  <footer class="letterhead__footer">
    <p class="letterhead__address">421, Address line here, 45452,Country Name</p>
    <div class="letterhead__rule"></div>
    <p class="letterhead__contact"><b>P:</b> 044-123 456 789 | <b>E:</b> info@webname.com &nbsp;| <b>W:</b> www.websitename.com</p>
  </footer>
</section>

<section class="signature">
  <div class="signature__details">
    <p class="signature__name">Daniel Marsh</p>
    <p class="signature__role">Managing Director</p>
    <p class="signature__address">421, Address line here, 45452Country Name</p>
    <p class="signature__contact"><b>P:</b> 044-123 456 789 | <b>E:</b> info@webname.com</p>
    <p class="signature__web">www.websitename.com</p>
  </div>
  <div class="signature__brand brand-name">Hollis Crest</div>
  <div class="signature__band">
    <span>Follow us on</span>
    <span class="social-list" aria-label="Social profiles">
      <svg width="15" height="15" viewBox="0 0 16 16"><circle cx="8" cy="8" r="7" fill="none" stroke="#2a2a2a" stroke-width="1.2"/></svg>
      <svg width="15" height="15" viewBox="0 0 16 16"><circle cx="8" cy="8" r="7" fill="none" stroke="#2a2a2a" stroke-width="1.2"/></svg>
      <svg width="15" height="15" viewBox="0 0 16 16"><circle cx="8" cy="8" r="7" fill="none" stroke="#2a2a2a" stroke-width="1.2"/></svg>
      <svg width="15" height="15" viewBox="0 0 16 16"><circle cx="8" cy="8" r="7" fill="none" stroke="#2a2a2a" stroke-width="1.2"/></svg>
      <svg width="15" height="15" viewBox="0 0 16 16"><circle cx="8" cy="8" r="7" fill="none" stroke="#2a2a2a" stroke-width="1.2"/></svg>
    </span>
    <span>/ name</span>
  </div>
</section>

</body>
</html>
```